Corporate Identity Pack - LetterHead, Business Card, Envelope

We are looking for a clean, professional, and visually connected corporate identity set for our company "VELTA HOME" (Cleaning, Gardening, and Pest Control services).

The pack must include:

Business Card (front and back)
Envelope with recipient window on the right side (22x11)
A4 Letterhead

We provide:
Our final logo (PNG)
Three design references (Inspiration1, Inspiration2, Inspiration3) to spark ideas — but you are absolutely free to propose your own creative solutions based on these concepts.

What we want:
A clean, modern, and trustworthy style
A subtle but creative watermark or graphic detail on the letterhead (not too invasive)

The same visual "family feeling" across business card, envelope, and letterhead: designs must be different but clearly connected

Strong readability for all text and contact details

Use our brand colors (Navy Blue, Green, Orange/Red) in a smart, non-overloaded way

No strict limitations: we are open to creative proposals as long as they are coherent, elegant, and suitable for professional use

Technical specifications:
100% full A4 page layout (no accidental borders)

Deliver ready-to-print PDFs and vector files (AI, EPS)

Respect 5 mm safety margins

Standard sizes for A4, business card, envelope C6 with window at the right

Tone:
Modern – Clean – Elegant – Creative – Trustworthy

Target Market(s)

Professional businesses, property managers, condominium administrators, companies, clinics, and offices requiring cleaning, gardening, and pest control services. The design must convey trust, reliability, professionalism, and attention to detail.

Industry/Entity Type

Cleaning Services, Gardening Services, Pest Control Services

Colors
0054AA
0677BA
7BADD7
CADEEF
E8F1F8
59FF00
82FF00
B8FF75
E3FFCB
F4FFEA
EB3D1F
EC4F4E
F09395
F8D3D4
FCEDEE

Requirements
Must have
• Cohesive design across business card, letterhead, and envelope Clean, modern, professional look Use of brand colors: Navy Blue (main), Green, Orange/Red accents Letterhead must include a subtle watermark without interfering with text Envelope must be with a transparent window for recipient address visibility High readability of all text and contact details Proper alignment, no unnecessary margins (full A4 layout)
Nice to have
• Creative but discreet use of the checkmark from the logo as part of the background or watermark Slight variation or accent of color tones while respecting brand identity A clean visual accent that gives a sense of movement or dynamic professionalism (without being distracting) Icons for email, phone, and website on the business card (if stylistically appropriate)
Should not have
• Overuse of colors or rainbow effects Heavy backgrounds or complex textures that interfere with readability Fonts that are too playful, comic-style, or non-professional Overcrowded layouts — the design must feel clean and spacious Watermarks that are too strong or central (they must be subtle and marginal)

```html
<!DOCTYPE html>
<html lang="en">
<head>
<meta charset="utf-8">
<title>Velta Home – Stationery Set</title>
<link href="https://fonts.googleapis.com/css2?family=Montserrat:wght@500;700;800&family=Open+Sans:wght@400;600&family=Roboto:wght@400;500&display=swap" rel="stylesheet">
<style>
  :root{
    --navy:#28255f;
    --navy-deep:#221f55;
    --green:#6cbf3a;
    --orange:#ef6a23;
    --paper:#ffffff;
    --stage:#ececee;
    --ink:#3a3a3a;
    --muted:#6a6a6a;
    --ghost:#dcdcdf;
    --wash-navy:#e6e5f0;
    --wash-green:#f1f7ec;
  }
  *{margin:0;padding:0;box-sizing:border-box}
  html,body{width:1200px;height:1000px;overflow:hidden}
  body{background:var(--stage);position:relative;font-family:"Open Sans",Arial,sans-serif;color:var(--ink)}
  .piece{position:absolute;background:var(--paper);overflow:hidden}

  .brand-name{font-family:"Montserrat",Arial,sans-serif;font-weight:700;color:var(--navy);white-space:nowrap;letter-spacing:.5px;display:flex;align-items:center;gap:8px}
  .brand-square{display:inline-block;background:var(--navy)}

  .band{position:absolute;left:0;right:0;bottom:0;background:var(--navy);color:#fff;font-family:"Montserrat",Arial,sans-serif;font-weight:700;display:flex;align-items:center;justify-content:center;letter-spacing:.4px}
  .band-chip{position:absolute;left:0;top:0;bottom:0;background:var(--green)}

  /* business card front */
  .card-front{left:191px;top:73px;width:378px;height:216px}
  .card-front .brand-name{position:absolute;left:68px;top:30px;font-size:27px}
  .card-front .brand-square{width:26px;height:26px}
  .holder{position:absolute;right:210px;top:103px;text-align:right;font-family:"Montserrat",Arial,sans-serif}
  .holder-name{color:var(--navy);font-weight:700;font-size:14px;letter-spacing:.3px}
  .holder-role{color:var(--green);font-weight:500;font-size:11px;margin-top:1px}
  .card-contact{position:absolute;left:206px;top:100px;font-family:"Roboto",Arial,sans-serif;font-size:10.5px;color:#333;line-height:14px}
  .card-contact .gap{height:6px}
  .contact-line{display:flex;align-items:center;gap:4px}
  .contact-line svg{width:10px;height:10px;fill:var(--navy)}
  .card-front .band{height:21px;font-size:8.5px}
  .card-front .band-chip{width:16px}

  /* business card back */
  .card-back{left:191px;top:298px;width:378px;height:217px;background:var(--navy-deep)}
  .card-back .pattern{position:absolute;inset:0;background:linear-gradient(135deg,#3b3878 0%,#2d2a68 55%,#221f55 100%)}

  /* emboss lockup */
  .emboss{position:absolute;left:210px;top:592px}
  .emboss .brand-name{color:var(--ghost);font-size:36px;font-weight:700}
  .emboss .brand-square{width:40px;height:40px;background:var(--ghost)}

  /* letterhead */
  .letterhead{left:616px;top:73px;width:474px;height:610px}
  .letterhead .brand-name{position:absolute;left:46px;top:53px;font-size:18px;gap:6px}
  .letterhead .brand-square{width:24px;height:24px}
  .lh-contact{position:absolute;left:332px;top:34px;font-family:"Roboto",Arial,sans-serif;font-size:8px;color:#444;line-height:10.5px}
  .lh-contact .gap{height:6px}
  .lh-contact .contact-line svg{width:7px;height:7px}
  .watermark{position:absolute;left:124px;top:220px;width:228px;height:198px;background:linear-gradient(160deg,var(--wash-navy) 0%,#efeff5 55%,var(--wash-green) 100%);opacity:.8}
  .letter-body{position:absolute;left:48px;top:155px;width:378px;font-size:7.2px;line-height:9.7px;color:#555;text-align:justify}
  .letter-body p{margin-bottom:9.7px}
  .signoff{position:absolute;left:48px;top:440px;font-size:7.2px;line-height:9.7px;color:#555}
  .signature{position:absolute;left:48px;top:474px;width:44px;height:34px;background:#ececec}
  .letterhead .band{height:27px;font-size:10px}
  .letterhead .band-chip{width:22px}

  /* envelope back */
  .env-back{left:104px;top:703px;width:479px;height:224px}
  .flap{position:absolute;left:0;top:0;width:479px;height:90px}
  .env-back .brand-name{position:absolute;left:171px;top:28px;font-size:18px;color:#fff;gap:6px}
  .env-back .brand-square{width:22px;height:22px;background:#fff}

  /* envelope front */
  .env-front{left:616px;top:703px;width:479px;height:224px}
  .env-front .brand-name{position:absolute;left:30px;top:35px;font-size:18px}
  .env-address{position:absolute;left:55px;top:57px;font-family:"Roboto",Arial,sans-serif;font-size:8.5px;color:#333;line-height:10.5px}
  .env-mark{position:absolute;left:287px;top:7px;width:187px;height:185px;background:linear-gradient(160deg,var(--wash-navy) 0%,#ededf3 60%,var(--wash-green) 100%)}
  .env-window{position:absolute;left:322px;top:124px;width:118px;height:47px;border-radius:4px;background:linear-gradient(180deg,#f3f3f4,#d9d9db);border:1px solid #d0d0d3}
  .env-front .band{height:27px;font-size:10px}
  .env-front .band-chip{width:24px}
</style>
</head>
<body>

<svg width="0" height="0" style="position:absolute">
  <symbol id="icon-phone" viewBox="0 0 24 24"><path d="M6.6 10.8a15.1 15.1 0 0 0 6.6 6.6l2.2-2.2a1 1 0 0 1 1-.25 11.4 11.4 0 0 0 3.6.57 1 1 0 0 1 1 1V20a1 1 0 0 1-1 1A17 17 0 0 1 3 4a1 1 0 0 1 1-1h3.5a1 1 0 0 1 1 1c0 1.25.2 2.45.57 3.6a1 1 0 0 1-.25 1z"/></symbol>
  <symbol id="icon-mail" viewBox="0 0 24 24"><path d="M2 5h20v14H2zm2 2v.5l8 5 8-5V7zm0 2.8V17h16V9.8l-8 5z"/></symbol>
  <symbol id="icon-web" viewBox="0 0 24 24"><path d="M12 2a10 10 0 1 0 0 20 10 10 0 0 0 0-20zm6.9 6h-2.9a15.7 15.7 0 0 0-1.4-3.6A8 8 0 0 1 18.9 8zM12 4a14 14 0 0 1 1.9 4h-3.8A14 14 0 0 1 12 4zM4.3 14a8.2 8.2 0 0 1 0-4h3.4a16.5 16.5 0 0 0 0 4zm.8 2h2.9a15.7 15.7 0 0 0 1.4 3.6A8 8 0 0 1 5.1 16zM8 8H5.1a8 8 0 0 1 4.3-3.6A15.7 15.7 0 0 0 8 8zm4 12a14 14 0 0 1-1.9-4h3.8A14 14 0 0 1 12 20zm2.3-6H9.7a14.7 14.7 0 0 1 0-4h4.6a14.7 14.7 0 0 1 0 4zm.3 5.6a15.7 15.7 0 0 0 1.4-3.6h2.9a8 8 0 0 1-4.3 3.6zm1.7-5.6a16.5 16.5 0 0 0 0-4h3.4a8.2 8.2 0 0 1 0 4z"/></symbol>
</svg>

<!-- Business card front -->
<section class="piece card-front">
  <div class="brand-name"><span class="brand-square"></span>VELTA HOME</div>
  <div class="holder">
    <div class="holder-name">DARA OLSEN</div>
    <div class="holder-role">Founder &amp; CEO</div>
  </div>
  <div class="card-contact">
    <div>48 Elm Avenue, Suite 5</div>
    <div>Lowell, MA 01850 USA</div>
    <div class="gap"></div>
    <div class="contact-line"><svg><use href="#icon-phone"/></svg>+39 347 5512083</div>
    <div class="contact-line"><svg><use href="#icon-mail"/></svg>office@velta-home.srl</div>
    <div class="contact-line"><svg><use href="#icon-web"/></svg>www.velta-home.srl</div>
  </div>
  <div class="band"><span class="band-chip"></span>CLEANING•GARDENING•PESTCONTROL</div>
</section>

<!-- Business card back -->
<section class="piece card-back">
  <div class="pattern" role="img" aria-label="Grid of embossed brand tiles on navy, with one tile in full brand colours"></div>
</section>

<!-- Embossed lockup -->
<div class="emboss">
  <div class="brand-name"><span class="brand-square"></span>VELTA HOME</div>
</div>

<!-- Letterhead -->
<section class="piece letterhead">
  <div class="brand-name"><span class="brand-square"></span>VELTA HOME</div>
  <div class="lh-contact">
    <div>48 Elm Avenue, Suite 5</div>
    <div>Lowell, MA 01850</div>
    <div class="gap"></div>
    <div class="contact-line"><svg><use href="#icon-phone"/></svg>+39 347 5512083</div>
    <div class="contact-line"><svg><use href="#icon-mail"/></svg>office@velta-home.srl</div>
    <div class="contact-line"><svg><use href="#icon-web"/></svg>www.velta-home.srl</div>
  </div>
  <div class="watermark" role="img" aria-label="Faint brand watermark behind the letter text"></div>
  <div class="letter-body">
    <p>Dear customer,</p>
    <p>Lorem ipsum dolor sit amet, consectetur adipisicing elit, sed do eiusmod tempor incididunt ut labore et dolore magna aliqua. Ut enim ad minim veniam, quis nostrud exercitation ullamco laboris nisi ut aliquip ex ea commodo consequat. Duis aute irure dolor in reprehenderit in voluptate velit esse cillum dolore eu fugiat nulla pariatur. Excepteur sint occaecat cupidatat non proident, sunt in culpa qui officia deserunt mollit anim id est laborum.</p>
    <p>Lorem ipsum dolor sit amet, consectetur adipisicing elit, sed do eiusmod tempor incididunt ut labore et dolore magna aliqua. Ut enim ad minim veniam, quis nostrud exercitation ullamco laboris nisi ut aliquip ex ea commodo consequat. Duis aute irure dolor in reprehenderit in voluptate velit esse cillum dolore eu fugiat nulla pariatur. Excepteur sint occaecat cupidatat non proident, sunt in culpa qui officia deserunt mollit anim id est laborum.</p>
    <p>Lorem ipsum dolor sit amet, consectetur adipisicing elit, sed do eiusmod tempor incididunt ut labore et dolore magna aliqua. Ut enim ad minim veniam, quis nostrud exercitation ullamco laboris nisi ut aliquip ex ea commodo consequat. Duis aute irure dolor in reprehenderit in voluptate velit esse cillum dolore eu fugiat nulla pariatur. Excepteur sint occaecat cupidatat non proident, sunt in culpa qui officia deserunt mollit anim id est laborum.</p>
    <p>Lorem ipsum dolor sit amet, consectetur adipisicing elit, sed do eiusmod tempor incididunt ut labore et dolore magna aliqua. Ut enim ad minim veniam, quis nostrud exercitation ullamco laboris nisi ut aliquip ex ea commodo consequat. Duis aute irure dolor in reprehenderit.</p>
    <p>Yours Sincerely,</p>
  </div>
  <div class="signoff">Peter Lund<br>General Director</div>
  <div class="signature" role="img" aria-label="Handwritten signature"></div>
  <div class="band"><span class="band-chip"></span>CLEANING•GARDENING•PESTCONTROL</div>
</section>

<!-- Envelope back -->
<section class="piece env-back">
  <svg class="flap" viewBox="0 0 479 90" preserveAspectRatio="none">
    <path d="M0 0H479V14L358 74Q339 84 318 84H161Q140 84 121 74L0 14Z" fill="var(--navy)"/>
    <path d="M8 20L121 80Q140 90 161 90H318Q339 90 358 80L471 20" fill="none" stroke="#e2e2e4" stroke-width="1"/>
  </svg>
  <div class="brand-name"><span class="brand-square"></span>VELTA HOME</div>
</section>

<!-- Envelope front -->
<section class="piece env-front">
  <div class="env-mark" role="img" aria-label="Faint brand watermark on the right of the envelope"></div>
  <div class="brand-name">VELTA HOME</div>
  <div class="env-address">48 Elm Avenue, Suite 5<br>Lowell, MA 01850 USA</div>
  <div class="env-window"></div>
  <div class="band"><span class="band-chip"></span>CLEANING•GARDENING•PESTCONTROL</div>
</section>

</body>
</html>
```